Dalton Perriwether breaking. Or D. Perriwether breaking

I break in and train horses, any age any bread of horse, for any disaplin. I need a business card that is simple but effective, in the way of looking professional. I would like a horse on my card, preferably a horse without a rider. I also pre train horse, younge horses that need a bit of riding before they go into serious work, and prepare yearlings for sale.

Reason: This is for my boyfriend, and I really want it to be perfect and impressive!

Target Market(s)

Thoroughbred race horse trainers, horse industrie people.

Industry/Entity Type

Business

Contact Information for Business Card

Dalton Perriwether horse breaking, "WOLLOMBEE" Kellerton, give your horse the right start to any career. dperri@mailzone.com.au, 0481392067. Horse breaking~pre-training~sale preparation

```html
<!DOCTYPE html>
<html lang="en">
<head>
<meta charset="utf-8">
<title>Dalton Perriwether – Horse Breaker business card</title>
<link rel="stylesheet" href="https://fonts.googleapis.com/css2?family=Open+Sans:wght@400;600;700&display=swap">
<style>
  :root {
    --page-bg: #d9dcd6;
    --card-green: #34512a;
    --card-green-deep: #2a4322;
    --band-dark: rgba(20, 34, 16, 0.55);
    --accent-lime: #9ad35e;
    --text-light: #eef3e8;
    --text-soft: #c9d6bf;
    --photo-leaf: #4f8a2e;
    --photo-shade: #2b4a1c;
    --photo-coat: #b57a45;
  }
  * { box-sizing: border-box; margin: 0; padding: 0; }
  html, body {
    width: 1200px; height: 900px; overflow: hidden;
    background: var(--page-bg);
    font-family: "Open Sans", Arial, sans-serif;
  }
  .canvas {
    width: 1200px; height: 900px;
    display: flex; flex-direction: column;
    align-items: center; justify-content: center; gap: 40px;
  }
  .card {
    position: relative;
    width: 660px; height: 400px;
    overflow: hidden;
    background: linear-gradient(160deg, var(--card-green) 0%, var(--card-green-deep) 100%);
    color: var(--text-light);
  }

  /* back side */
  .card-back .services {
    position: absolute; top: 58px; right: 0;
    padding: 12px 34px 12px 60px;
    background: var(--band-dark);
    font-size: 15px; letter-spacing: 0.4px;
  }
  .card-back .divider-band {
    position: absolute; top: 118px; right: 150px;
    width: 200px; height: 22px;
    background: var(--band-dark);
  }
  .card-back .tagline {
    position: absolute; bottom: 70px; left: 0;
    padding: 12px 40px 12px 36px;
    background: var(--band-dark);
    font-size: 16px; font-style: italic; letter-spacing: 0.3px;
  }

  /* front side */
  .card-front .photo {
    position: absolute; left: 0; top: 0;
    width: 56%; height: 100%;
    background:
      radial-gradient(ellipse 40% 35% at 48% 58%, var(--photo-coat) 0%, rgba(181,122,69,0) 100%),
      linear-gradient(180deg, var(--photo-shade) 0%, var(--photo-leaf) 55%, #6aa83a 100%);
  }
  .card-front .light-edge {
    position: absolute; top: 0; left: 56%;
    width: 3px; height: 100%;
    background: linear-gradient(180deg, rgba(154,211,94,0.9), rgba(154,211,94,0.2));
    box-shadow: 0 0 14px rgba(154,211,94,0.6);
  }
  .card-front .identity {
    position: absolute; top: 52px; left: calc(56% + 26px);
  }
  .identity .name {
    font-size: 22px; font-weight: 700; line-height: 1.1;
  }
  .identity .role {
    margin-top: 4px; font-size: 13px; color: var(--text-soft);
  }
  .card-front .contacts {
    position: absolute; top: 118px; right: 28px;
    list-style: none; text-align: right;
    font-size: 13px; line-height: 1.4;
  }
  .contacts li {
    display: flex; align-items: center; justify-content: flex-end;
    gap: 10px; margin-bottom: 12px;
  }
  .contacts svg { width: 15px; height: 15px; flex: none; }
  .card-front .footer-band {
    position: absolute; left: 56%; right: 0; bottom: 0;
    height: 46px;
    background: var(--band-dark);
  }
</style>
</head>
<body>
<main class="canvas">

  <section class="card card-back" aria-label="Card back">
    <p class="services">Horse breaking | Pre-training | Sale preparation</p>
    <div class="divider-band"></div>
    <p class="tagline">“Give your horse the right start to any career.”</p>
  </section>

  <section class="card card-front" aria-label="Card front">
    <div class="photo" role="img" aria-label="Photograph of a chestnut foal with a white blaze standing in green grass before trees"></div>
    <div class="light-edge"></div>
    <div class="identity">
      <h1 class="name">Dalton Perriwether</h1>
      <p class="role">Horse Breaker</p>
    </div>
    <ul class="contacts">
      <li>0481 392 067
        <svg viewBox="0 0 24 24" aria-hidden="true"><path fill="var(--accent-lime)" d="M6.6 10.8a15 15 0 0 0 6.6 6.6l2.2-2.2a1 1 0 0 1 1-.25 11.4 11.4 0 0 0 3.6.57 1 1 0 0 1 1 1V20a1 1 0 0 1-1 1A17 17 0 0 1 3 4a1 1 0 0 1 1-1h3.5a1 1 0 0 1 1 1c0 1.25.2 2.45.57 3.57a1 1 0 0 1-.25 1z"/></svg>
      </li>
      <li>dperri@mailzone.com.au
        <svg viewBox="0 0 24 24" aria-hidden="true"><rect x="2" y="5" width="20" height="14" rx="1.5" fill="var(--accent-lime)"/><path d="M3 6l9 7 9-7" fill="none" stroke="var(--card-green-deep)" stroke-width="1.6"/></svg>
      </li>
      <li>“WOLLOMBEE” Kellerton
        <svg viewBox="0 0 24 24" aria-hidden="true"><path fill="var(--accent-lime)" d="M12 2a7 7 0 0 0-7 7c0 5.2 7 13 7 13s7-7.8 7-13a7 7 0 0 0-7-7zm0 9.5A2.5 2.5 0 1 1 12 6.5a2.5 2.5 0 0 1 0 5z"/></svg>
      </li>
    </ul>
    <div class="footer-band"></div>
  </section>

</main>
</body>
</html>
```